Web Design Project: Facility Management company

Hi! We need a new website.

Our current website: http://www.brantel-group.ru/ and we don-t like it. =)
The structure of our company has changed and now we don't need "cleaning" and "engeneering" on this site.

We are facility management company in Russia. So we provide integrated service solutions specific to industrial services: maintenance, repair, etc. of engineering systems.
More services:
Energy planning
Automation
Audit
Statements with regulators
Video surveillance
Central heating
Security systems
Welding
Management of subcontractors
Electrical installation and service needs
Reception
Catering

Visitors:
* Managers in the field of commercial real estate
* Chief engineers
* TOP managers of large companies, malls, factories...
+ their subordinates
* Small% of applicants.

Here you can see some websites/patterns we liked:
http://www.kvelmort.ru/ (This is our competitor’s site, so our site shouldn’t be an exact copy))))
http://www.orbitask.ru/
http://www.layoutpinery.com/demo/24296.html
http://www.layoutpinery.com/website-templates/10145.html

Style:
Light, hi-tech/minimalizm, the color palette should be based on the original site colors (Green + black + white). http://www.brantel-group.ru/

Estimated sitemap:
1. Home
2. About Us
3. Company's policy
4. History + Achievements.
5. Certificates
6. Map of presence (Here you can use sample map in file "our projects")
7. Services
8. Portfolio
9. News or blog
10. Jobs
11. Contacts - with the feedback form (or the function "call to order")
12. English

Need a design pages: main page, page 404. The rest of the page could be created by general pattern.

Logo, navigation bar and contacts should be visible on all pages of a site.
Flash animation elements and buttons, etc. - not needed.

* We need to develop 3 websites, so we are looking for a long term cooperation.
Looking forward to your creativity =)

Must Have:
Clear, intuitive structure of web pages.
In the center - of pictures reflecting our main services (industrial theme). May be in rotation.
BUT! This banner (central picture) should not be a huge one =)
All relevant information should be visible at once without scrolling.

A possibility to place media files (presentations, video ...) and 2 banner links on the main page.

Font should be available in Cyrillic.
Updates

IMPORTANT!

Please notice that in thisdesign we don't need "cleaning" and "engeneering" on this site.

So don't use old block of 4pictures from our current website. We don't need it anymore. 

Thestructure of our company has changed and now we need some links (may be banners,may be something else) to our future cleaning website as well as engeneeringwebsite.
It should look like seperate (partner) companies, not like our sevices.

Regards, Vera.

Please don't forget that we need bilingual site.

So define language changing tool in your designs.

Industry/Entity Type

Industrial

```html
<!DOCTYPE html>
<html lang="en">
<head>
<meta charset="utf-8">
<title>Brantel — Facility Management</title>
<link rel="stylesheet" href="https://fonts.googleapis.com/css2?family=Open+Sans:wght@300;400;600;700;800&display=swap">
<style>
:root{
  --nav-line:#3a3a3a;
  --green:#6f8a2e;
  --green-light:#d3e08a;
  --ink:#222;
  --text:#555;
  --footer:#232323;
}
*{margin:0;padding:0;box-sizing:border-box}
html,body{width:1200px;height:1045px;overflow:hidden}
body{position:relative;font-family:'Open Sans',sans-serif;color:var(--text);
  background:linear-gradient(180deg,#fff 0,#fbfdf5 130px,#e9f1c8 330px,#d9e7a4 487px,#fff 488px,#fff 100%)}
.abs{position:absolute}

/* navigation */
.topbar{left:0;top:0;width:1200px;height:47px;background:linear-gradient(#2e2e2e,#1c1c1c)}
.nav{left:110px;top:5px;height:42px;display:flex;list-style:none}
.nav li{height:42px;display:flex;align-items:center;padding:0 11.5px;border-right:1px solid var(--nav-line);
  font-size:12.5px;font-weight:600;color:#f2f2f2;text-transform:uppercase;letter-spacing:-.3px;white-space:nowrap}
.nav li.active{background:linear-gradient(#fdfef8,#e4edc4);color:var(--green);padding:0 16px;border-right:0}

/* header */
.brand{left:112px;top:86px;display:flex;align-items:center;gap:14px}
.brand-mark{width:30px;height:30px;background:var(--ink)}
.brand-name{font-size:40px;font-weight:400;letter-spacing:7px;color:var(--ink)}
.search{left:778px;top:74px;width:233px;height:28px;display:flex}
.search-field{flex:1;border:1px solid #d8d8d8;background:#fff;font-size:11px;color:#888;padding:6px 9px}
.search-btn{width:27px;height:28px;background:#6e8a2a}
.lang{left:1024px;top:74px;width:67px;height:28px;background:linear-gradient(#f6a21e,#ea7d05);
  color:#fff;font-size:12px;font-weight:600;display:flex;align-items:center;justify-content:center;border-radius:2px}
.helpline{right:109px;top:120px;display:flex;align-items:center;gap:9px;font-size:23px;font-weight:500;color:#222}
.helpline strong{font-weight:500;font-size:25px}

/* hero */
.hero-frame{left:110px;top:174px;width:980px;height:357px;background:#fff;border:1px solid #dcdcdc;box-shadow:0 0 6px rgba(0,0,0,.08)}
.hero-visual{left:126px;top:190px;width:948px;height:324px;
  background:linear-gradient(90deg,#a3b15a 0,#8f9e47 40%,#7b8a35 100%)}
.hero-title{left:474px;top:284px;font-size:40px;font-weight:800;color:#fff;white-space:nowrap}
.hero-text{left:477px;top:341px;font-size:15px;line-height:24px;color:#fff;white-space:nowrap}

/* partner banners */
.partner{top:552px;width:481px;height:83px;border:1px solid #b9c3cf;overflow:hidden}
.partner-cleaning{left:110px;background:linear-gradient(90deg,#8ea6c0,#a6bcd8 45%)}
.partner-engineering{left:609px;background:linear-gradient(90deg,#e0d79a,#d6d5cc 45%,#b7b7a8);border-color:#c5c5bb}
.partner-title{right:20px;top:12px;font-size:19.5px;font-weight:700;text-transform:uppercase;letter-spacing:.4px;white-space:nowrap}
.partner-cleaning .partner-title{color:#1d4650}
.partner-engineering .partner-title{color:#3a3a3a}
.partner-btn{top:44px;height:24px;padding:0 9px;background:#2f2f2f;border-radius:2px;color:#fff;
  font-size:11px;font-weight:600;display:flex;align-items:center;gap:5px;white-space:nowrap}
.partner-cleaning .partner-btn{right:96px}
.partner-engineering .partner-btn{right:30px}

/* intro */
.intro-title{left:110px;top:658px;font-size:23px;font-weight:400;color:var(--green);white-space:nowrap}
.features{left:110px;top:700px;list-style:none}
.features li{font-size:13px;font-weight:600;color:#444;line-height:22px;display:flex;align-items:center;gap:7px}
.coverage-map{left:488px;top:692px;width:194px;height:152px;background:linear-gradient(180deg,#c8eb96,#a8dd6a)}
.intro-text{left:110px;font-size:12px;line-height:20px;color:#555;white-space:nowrap}

/* news */
.news-head{left:776px;top:660px;width:314px;height:46px;background:var(--green-light);border:1px solid #c3d075;
  font-size:18px;font-weight:600;color:#222;padding:12px 15px}
.news-body{left:776px;top:706px;width:314px;height:240px;background:linear-gradient(#eef0ea,#fff 70%)}
.news-item{left:791px;width:290px;display:flex;gap:13px}
.news-date{width:40px;height:46px;background:var(--green-light);clip-path:polygon(0 0,100% 0,100% 75%,50% 100%,0 75%);
  font-size:12px;color:#333;text-align:center;line-height:16px;padding-top:4px;flex:none}
.news-copy{font-size:12px;line-height:20px;color:#555}
.news-copy b{display:block;font-weight:600;color:#333;font-size:12px;margin-top:-4px}

/* footer */
.footer{left:0;top:981px;width:1200px;height:64px;background:var(--footer);text-align:center;font-size:12px;color:#8a8a8a}
.footer-links{padding-top:14px}
.footer-links span{color:#666;margin:0 2px}
.footer-copy{margin-top:3px;color:#999}
</style>
</head>
<body>

<div class="abs topbar"></div>
<ul class="abs nav">
  <li class="active">Home</li>
  <li>About us</li>
  <li>Company's policy</li>
  <li>History + Certificates</li>
  <li>Map</li>
  <li>Services</li>
  <li>Portfolio</li>
  <li>News/Blog</li>
  <li>Jobs</li>
  <li>Contact&nbsp; us</li>
</ul>

<div class="abs brand">
  <span class="brand-mark"></span>
  <span class="brand-name">BRANTEL</span>
</div>

<div class="abs search">
  <div class="search-field">Enter a keyword...</div>
  <div class="search-btn">
    <svg width="27" height="28" viewBox="0 0 27 28"><circle cx="12" cy="12" r="7" fill="none" stroke="#fff" stroke-width="2.5"/><line x1="17" y1="17" x2="23" y2="23" stroke="#fff" stroke-width="3"/></svg>
  </div>
</div>
<div class="abs lang">Русский</div>

<div class="abs helpline">
  <span>Need Help? Call us on:</span>
  <svg width="20" height="26" viewBox="0 0 20 26"><path d="M6 2c-4 3-5 10-1 17 2 4 6 6 9 4l2-2-4-5-3 2c-2-2-3-6-2-9l3-1-1-6z" fill="#7d9a2e"/></svg>
  <strong>+7 812 555 0143</strong>
</div>

<div class="abs hero-frame"></div>
<div class="abs hero-visual" role="img" aria-label="Photo of an engineer in a hard hat and safety vest in front of office towers"></div>
<div class="abs hero-title">Quality services on time...</div>
<p class="abs hero-text">We use an accumulated experience of immovable property maintenance, any<br>kind of engineering systems, and their modernization for extension of durability<br>time, and you save your money.</p>

<div class="abs partner partner-cleaning" role="img" aria-label="Photo of a window cleaner on a glass facade">
  <div class="abs partner-title">Professional cleaning</div>
  <div class="abs partner-btn">CLICK HERE TO KNOW MORE
    <svg width="7" height="10" viewBox="0 0 7 10"><path d="M1 1l4 4-4 4" fill="none" stroke="#fff" stroke-width="2"/></svg></div>
</div>
<div class="abs partner partner-engineering" role="img" aria-label="Photo of a hard hat on rolled blueprints">
  <div class="abs partner-title">Civil engineering</div>
  <div class="abs partner-btn">CLICK HERE TO KNOW MORE
    <svg width="7" height="10" viewBox="0 0 7 10"><path d="M1 1l4 4-4 4" fill="none" stroke="#fff" stroke-width="2"/></svg></div>
</div>

<h1 class="abs intro-title">BRANTEL TM &amp; FM COMPANY</h1>
<ul class="abs features">
  <li><svg width="9" height="8" viewBox="0 0 9 8"><path d="M1 4l2.5 2.5L8 1" fill="none" stroke="#4a6420" stroke-width="2"/></svg>Commercial property management</li>
  <li><svg width="9" height="8" viewBox="0 0 9 8"><path d="M1 4l2.5 2.5L8 1" fill="none" stroke="#4a6420" stroke-width="2"/></svg>Complex maintenance of immovable property</li>
  <li><svg width="9" height="8" viewBox="0 0 9 8"><path d="M1 4l2.5 2.5L8 1" fill="none" stroke="#4a6420" stroke-width="2"/></svg>Commercial property maintenance service</li>
</ul>
<div class="abs coverage-map" role="img" aria-label="Map of company presence with project locations marked"></div>
<p class="abs intro-text" style="top:779px">These are the most important aspects of acquisition of the<br>highest possible incomes from the commercial property object`s<br>operation regardless of their purpose: it can be production,<br>business center, a building of a shop, bank, restaurant,</p>
<p class="abs intro-text" style="top:863px">warehousing logistic complex, hotel or the biggest shopping and recreation center.</p>
<p class="abs intro-text" style="top:903px">More and more modern companies – proprietors and developer companies, hand over maintenance of the<br>buildings, structures with all installation for outsourcing to a professional management company.</p>

<div class="abs news-head">NEWS</div>
<div class="abs news-body"></div>
<div class="abs news-item" style="top:724px">
  <div class="news-date">SEP<br>12</div>
  <div class="news-copy"><b>Lorem ipsum dolor sit amet,</b>Consectetuer adipiscing elit, sed diam nonummy nibh euismod tincidunt ut.</div>
</div>
<div class="abs news-item" style="top:803px">
  <div class="news-date">SEP<br>10</div>
  <div class="news-copy"><b>Laoreet dolore&nbsp; magna aliquam erat</b>Ut wisi enim ad minim veniam, quis nostrud exerci tation ullamcorper.</div>
</div>
<div class="abs news-item" style="top:883px">
  <div class="news-date">SEP<br>5</div>
  <div class="news-copy"><b>Suscipit lobortis nisl ut aliquip ex ea</b>Commodo consequat. Duis autem vel eum iriure dolor in hendrerit.</div>
</div>

<footer class="abs footer">
  <div class="footer-links">Home <span>::</span> About us <span>::</span> Company's policy <span>::</span> History + Certificates <span>::</span> Services <span>::</span> Portfolio <span>::</span> News/blog <span>::</span> Jobs <span>::</span> Contact&nbsp; us</div>
  <div class="footer-copy">© Brantel 2010</div>
</footer>

</body>
</html>
```